■ 依頼の目的/概要
グループ企業内で使用する、業務支援ポータルサイトのリニューアルです。
依頼内容は、TOPページのデザイン作成です。
レイアウト案が2パターンありますので、制作要項をもとに、合計2パターンご提案をお願いします。
(制作要項:P3~4参照)

■現在の参考サイト
制作要項に、参考URLを掲載しております。詳しくは添付の制作要項を参照ください。

■現状の課題
・デザインが洗練されていない。
・情報を伝達、共有するツールとしては分かり難いレイアウトの為、社員に情報が伝わりにくい。
・メニューが煩雑になっており、従業員が必要な情報を探すときにも、目的にたどり着きにくい。

■ 重視する点/検討基準
① デザイン性(使いやすさ・見やすさ・親しみやすさ)
② 納期厳守

■ 具体的な制作数
TOPページ:2パターン(デザイン) *制作要項:P.3~4参照

■募集条件
キャラクターにつきましては、商標上の問題により、現在開示することが出来ないため、
アタリで作成をお願い致します。
デザイン選定後、当選者にキャラクターデザインをお渡ししますので、
差し込んで頂き、納品完了となります。
ご認識をお願いします。

■納品ファイル
・イラストレーター形式(.ai)
・フォトショップ形式(.psd)
*1 募集条件を満たした状態のデザイン
*2 納品のフォトショップは、できるだけレイヤー結合せず、コーディング時に部品として
扱えるようにしてください。こちらでも再加工できる状態でお願いします。

■選考の進め方
ご提案頂いたデザイン内容・コンセプトなどをもとに、プロジェクトメンバーで選考、決定致します。

皆様からの、素晴らしいご提案を、お待ちしております。
宜しくお願い致します。
この度、募集期間を5日間、延長させて頂きます。
また、依頼金額についても 50,000円 ⇒ 70,000円 に変更致します。

今一度、ご提案を頂ければ幸甚です。引き続き、よろしくお願いします。
こちらが要望するデザインイメージと、使用していただくデザインパーツを加えております。
改めて、ご参照頂ますよう、お願いします。
コンセプトに見合うデザインは、ご提案頂いておりますが、あと1日延長させて頂きます。
引き続き、皆様からのご提案をお待ちしております。
宜しくお願い致します。
たくさんのご提案ありがとうございます。
もうすこしパターンを見てみたいため、3日間延長いたします。

宜しくお願い致します。
度々申し訳御座いません。
幾つか、イメージに則したデザインをご提案頂いておりますが、
提案数が少ないので、再度延長致します。

見ていて楽しくなるようなポータルサイトデザインのご提案をお待ちしております。
引き続き宜しくお願い致します。
度々の延長により、ご迷惑をおかけしております。
今回、デザインについて、様々なパターンから検討したかったのですが、
思うように提案が集まらなかった為、依頼金額の追加、
及び期間の延長を行なっております。

情報不足により、皆様のデザインスキルを引き出すことができなかったと思い、
今回、募集要項に、開示できる限りの情報を添えて、更新しております。
ご参照頂ければ幸いです。

皆様からの素晴らしい提案をお待ちしております。
お世話になっております。
度々、申し訳ございませんが、1週間延長致します。
開示可能な情報が少ない為、提案するに出来ない状況なのでは無いかと
思いますが、必要な情報や、ご質問等御座いましたら、お気軽にお申し
付けください。

宜しくお願い致します。
度々申し訳御座いません。
再度1週間延長します。
素晴らしい提案を頂いておりますが、採用にまでは至っていない状況です。

ポータルサイトの用途を伝えきれていないかもしれませんので、
基本機能を、以下に明示します。

①サービス窓口のオペレータが、お客様へ案内する際に活用できるサービス情報データベース
②研修担当者が新人教育・研修時に活用できるマニュアル等の教育支援ツール
③新人社員が、空いた時間にテストやマニュアルなどを活用できる自己学習支援ツール
④目標などの数値関連を開示し、他のオペレータとの競争環境をつくり上げる、目標支援ツール
⑤対応時に手本となる音声データや対応時の良い台本などが拝聴・閲覧ができるスキルアップ支援ツール
⑥オペレータが業務において、疑問点や不明点、改善提案などを行い、実際にサービス運営陣も回答ができるFAQツール

上記の6点を利用でき、アクセス数を伸ばせるような、クオリティの高いポータルサイトデザインを募集致します。

ご質問のある方は、メッセージにて個別に回答致しますので、お気軽にお申し付けください。

引き続き、宜しくお願い致します。
本依頼に対しまして、お忙しい中、数々のデザインをご提案頂き、
誠にありがとうございました。
皆様からご提案頂いた貴重なデザイン案は、現在こちらで検討させて
頂いております。

今回の依頼は、スタート時点から、具体的な完成形が見えにくい依頼と
なっており、募集期限が大幅に伸び、Toviraの皆様方にはご迷惑をお掛け
致しました。
申し訳ございませんでした。

つきましては、完成形により具体性を持たせるため、弊社でデザインイメージを
作成致しました。
お手数をお掛けしますが、修正箇所は添付ファイルのデザインイメージ下部に
記載しておりますので、ご確認をお願い致します。

また、恐れ入りますが、依頼期限は12/28(金)まで、延長させて頂きたいと
思います。
素敵なデザイン案を、ご検討頂けますと幸甚です。

宜しくお願い申し上げます。

こちらの要望した、楽しげで、飽きの来ないデザインに加え、
ピンクを基調としたサイトカラーと、フェルト調のデザインパーツが
マッチしており、細部にこだわりを感じられるデザインになっていました。

まず、今回の依頼について、こちらの要望がうまく定まらず、ご迷惑をお掛けしたこと、お詫び申し上げます。
また、度重なる延長にも関わらず、ご協力頂きましたトヴィラの皆さまに感謝致します。誠にありがとうございました。

今後も、Tovirasを通して仕事を依頼する機会があるかと思いますが、その際はまた、素晴らしいご提案を頂ければ幸甚でございます。

```html
<!DOCTYPE html>
<html lang="ja">
<head>
<meta charset="utf-8">
<title>CREST Portal</title>
<link href="https://fonts.googleapis.com/css2?family=Noto+Sans+JP:wght@400;700&display=swap" rel="stylesheet">
<style>
:root{
  --navy:#24367e;
  --blue:#3a5cb8;
  --link:#2a56c6;
  --line:#c9d3e6;
  --pale:#eef3fb;
  --bg:#f6f8fc;
  --foot:#3b2f72;
  --tips:#8fae2e;
  --text:#333;
}
*{box-sizing:border-box;margin:0;padding:0}
html,body{width:766px;height:1200px;overflow:hidden}
body{font-family:"Noto Sans JP",sans-serif;color:var(--text);background:var(--bg);font-size:9px;position:relative}
.site-header{height:56px;background:#fff;position:relative}
.brand{position:absolute;left:46px;top:14px;display:flex;align-items:center;gap:6px;font-size:20px;font-weight:700;color:var(--navy);line-height:1.2}
.brand i{display:block;width:14px;height:14px;background:var(--navy)}
.brand small{display:block;font-size:7px;font-weight:400;color:#888;position:absolute;top:27px;left:20px;white-space:nowrap}
.character-slot{position:absolute;right:46px;top:8px;width:150px;height:28px;border:1px solid #aab;display:flex;align-items:center;justify-content:center;font-size:12px;color:#555;border-radius:4px;background:#fafafa}
.global-nav{height:34px;background:linear-gradient(#fff,#e3e9f5);border-top:1px solid var(--line);border-bottom:3px solid var(--navy)}
.global-nav ul{list-style:none;display:flex;margin:0 46px;height:100%}
.global-nav li{flex:1;display:flex;align-items:center;justify-content:center;font-size:11px;font-weight:700;color:var(--navy);border-right:1px solid var(--line)}
.global-nav li:last-child{border-right:0}
.hero{position:absolute;left:46px;top:97px;width:674px;height:248px;background:linear-gradient(110deg,#1d3c8c 0%,#6f93d2 40%,#dbe6f4 70%,#f3f6fb 100%);overflow:hidden}
.hero-copy{position:absolute;left:222px;top:138px;width:200px;background:rgba(30,50,120,.75);color:#fff;font-size:15px;font-weight:700;line-height:1.35;padding:8px 12px}
.hero-btn{position:absolute;left:330px;top:218px;background:#2d3e86;color:#fff;font-size:10px;line-height:1.4;padding:3px 10px;border:1px solid #fff;white-space:nowrap}
.main{position:absolute;left:46px;top:357px;width:484px}
.side{position:absolute;left:550px;top:357px;width:170px}
.panel{background:#fff;border:1px solid var(--line);margin-bottom:16px}
.panel-head{display:flex;align-items:center;justify-content:space-between;height:26px;padding:0 8px;background:linear-gradient(#fff,#e8eef8);border-bottom:1px solid var(--line);font-size:11px;font-weight:700;color:var(--navy)}
.panel-head .more{font-size:8px;font-weight:400;color:#555;border:1px solid #bbb;padding:1px 6px;background:#fff}
.purpose{display:grid;grid-template-columns:1fr 1fr;height:140px}
.purpose-col{padding:8px 10px;font-size:8px}
.purpose-col:first-child{border-right:1px dotted var(--line)}
.purpose-col h3{font-size:9px;color:var(--navy);margin:2px 0 4px}
.purpose-col p{color:var(--link);margin:0 0 6px 8px}
.icon-grid{display:grid;grid-template-columns:1fr 1fr;gap:6px 4px;margin-top:4px}
.icon-grid span{display:flex;align-items:center;gap:4px;color:var(--link)}
.icon-grid b{display:block;width:18px;height:18px;border-radius:3px;background:#b9cbe9}
.news{list-style:none}
.news li{display:flex;gap:10px;height:28px;align-items:center;padding:0 8px;border-bottom:1px dotted var(--line);font-size:8px;white-space:nowrap;overflow:hidden}
.news li:last-child{border-bottom:0}
.news time{color:#555;width:52px;flex:none}
.news a{color:var(--link);text-decoration:none}
.search{display:flex;width:170px;height:20px;margin-bottom:16px}
.search input{flex:1;min-width:0;border:1px solid #aaa;border-right:0;background:#fff}
.search button{flex:none;width:40px;background:var(--navy);color:#fff;border:0;font-size:9px;line-height:20px;font-family:inherit}
.login{padding:10px;font-size:8px;height:182px}
.login label{display:block;margin-top:4px}
.login input{display:block;width:100%;height:16px;border:1px solid #aaa;margin:2px 0 6px}
.login button{width:100%;height:20px;background:var(--blue);color:#fff;border:0;font-family:inherit;font-size:9px;margin-top:6px}
.notice{height:86px}
.tips{border:1px solid var(--tips);background:#fff}
.tips h3{background:#eaf3cf;color:var(--tips);font-size:11px;padding:3px 8px}
.tips p{padding:6px 8px;font-size:7.5px;line-height:1.55;color:#555}
.footer-links{position:absolute;left:46px;top:1142px;font-size:8px;color:var(--link);display:flex;gap:12px}
.site-footer{position:absolute;left:0;bottom:0;width:766px;height:22px;background:var(--foot);color:#cfc8ee;font-size:7px;line-height:22px;padding:0 46px}
</style>
</head>
<body>
<header class="site-header">
  <div class="brand"><i></i>CREST Portal<small>業務支援ポータル</small></div>
  <div class="character-slot">Character</div>
</header>
<nav class="global-nav">
  <ul><li>学習メニュー</li><li>機能を使う</li><li>業務周知</li><li>目標・成績</li><li>お問い合わせ</li></ul>
</nav>

<section class="hero" role="img" aria-label="ヘッドセットを付けたオペレーターと地球のビジュアル">
  <div class="hero-copy">遠隔操作で<br>お客様をサポート<br>いたします</div>
  <div class="hero-btn">詳細はこちら</div>
</section>

<main class="main">
  <section class="panel">
    <div class="panel-head">目的から探す</div>
    <div class="purpose">
      <div class="purpose-col">
        <h3>■ 探す一覧</h3>
        <div class="icon-grid">
          <span><b></b>研修資料</span><span><b></b>FAQ</span>
          <span><b></b>音声データ</span><span><b></b>マニュアル</span>
          <span><b></b>テスト</span>
        </div>
      </div>
      <div class="purpose-col">
        <h3>■ 学習メニュー</h3>
        <p>› 新人研修を受ける　› 復習用テストを受ける</p>
        <h3>■ 機能を使う</h3>
        <p>› メッセージボードを見る　› 台本を探す</p>
        <h3>■ お問い合わせ</h3>
        <p>› 疑問点を質問する　› 改善提案をする</p>
      </div>
    </div>
  </section>

  <section class="panel">
    <div class="panel-head">新着情報<span class="more">一覧</span></div>
    <ul class="news">
      <li><time>2012/12/20</time><a href="#">【運営局からのお知らせ】新着情報テキスト新着情報テキスト新着情報</a></li>
      <li><time>2012/12/19</time><a href="#">【運営局からのお知らせ】新着情報テキスト新着情報テキスト新着情報</a></li>
      <li><time>2012/12/18</time><a href="#">【運営局からのお知らせ】新着情報テキストが入ります</a></li>
      <li><time>2012/12/17</time><a href="#">【運営局からのお知らせ】新着情報テキストが入ります</a></li>
      <li><time>2012/12/14</time><a href="#">【運営局からのお知らせ】新着情報テキスト新着情報テキスト新着情報</a></li>
      <li><time>2012/12/13</time><a href="#">【運営局からのお知らせ】新着情報テキストが入ります</a></li>
      <li><time>2012/12/12</time><a href="#">【運営局からのお知らせ】新着情報テキストが入ります</a></li>
      <li><time>2012/12/11</time><a href="#">【運営局からのお知らせ】新着情報テキスト新着情報テキスト新着情報</a></li>
      <li><time>2012/12/10</time><a href="#">【運営局からのお知らせ】新着情報テキストが入ります</a></li>
    </ul>
  </section>

  <section class="panel">
    <div class="panel-head">障害情報<span class="more">一覧</span></div>
    <ul class="news">
      <li><time>2012/12/20</time><a href="#">【障害情報のお知らせ】障害情報テキスト障害情報テキスト障害情報</a></li>
      <li><time>2012/12/19</time><a href="#">【障害情報のお知らせ】障害情報テキスト障害情報テキスト障害情報</a></li>
      <li><time>2012/12/18</time><a href="#">【障害情報のお知らせ】障害情報テキストが入ります</a></li>
      <li><time>2012/12/17</time><a href="#">【障害情報のお知らせ】障害情報テキストが入ります</a></li>
      <li><time>2012/12/14</time><a href="#">【障害情報のお知らせ】障害情報テキスト障害情報テキスト障害情報</a></li>
      <li><time>2012/12/13</time><a href="#">【障害情報のお知らせ】障害情報テキストが入ります</a></li>
      <li><time>2012/12/12</time><a href="#">【障害情報のお知らせ】障害情報テキストが入ります</a></li>
      <li><time>2012/12/11</time><a href="#">【障害情報のお知らせ】障害情報テキスト障害情報テキスト障害情報</a></li>
    </ul>
  </section>
</main>

<aside class="side">
  <form class="search"><input type="text" aria-label="検索"><button type="button">検索</button></form>
  <section class="panel login">
    <label>ID</label><input type="text">
    <label>PW</label><input type="password">
    <button type="button">ログインする</button>
  </section>
  <section class="panel notice"></section>
  <section class="tips">
    <h3>Tips</h3>
    <p>FAQの検索は、キーワードを短く区切って入力すると目的の回答が見つかりやすくなります。よく使うページはお気に入りに登録しておきましょう。</p>
  </section>
</aside>

<nav class="footer-links"><span>トップページ</span><span>個人情報</span><span>運用規定</span><span>目標</span><span>お問い合わせ</span></nav>
<footer class="site-footer">©2012 CREST Co. All Rights Reserved.</footer>
</body>
</html>
```